Accounting business needs a fridge magnet design

I need a business card size design to be used as a fridge magnet.
It will need to be vertical not horizontal and it will have my logo and the services I provide listed below it.
It needs to be pleasing to the eye and catch peoples attention.
I have uploaded my current business card as a reference.
It can look totally different though, i am open to new ideas.

It will need to say:

Specialising in:
*Small Business Taxation
*Company & Trust Returns
*Financial Statements
*Partnership Taxation
*BAS preparation/lodgement
*Capital Gains Tax
*Business Start Ups
*Business Structuring
*Tax Planning

```html
<!DOCTYPE html>
<html lang="en">
<head>
<meta charset="utf-8">
<title>Nilpoint Tax – Fridge Magnet</title>
<link href="https://fonts.googleapis.com/css2?family=Montserrat:wght@400;500;700&display=swap" rel="stylesheet">
<style>
  :root {
    --backdrop: #5a5a5a;
    --ink-black: #201f1e;
    --brand-blue: #22b0e3;
    --text-dark: #1d2a33;
    --white: #ffffff;
    --badge-gold: #f5d20a;
    --badge-navy: #1c5aa8;
  }
  * { margin: 0; padding: 0; box-sizing: border-box; }
  html, body {
    width: 1200px; height: 1200px; overflow: hidden;
    background: var(--backdrop);
    font-family: "Montserrat", sans-serif;
  }
  .magnet {
    position: absolute; left: 312px; top: 95px;
    width: 576px; height: 1009px;
    background: var(--white);
    overflow: hidden;
  }
  .magnet__shapes { position: absolute; inset: 0; }
  .abs { position: absolute; left: 0; width: 100%; text-align: center; }
  .brand-name {
    top: 200px; color: var(--white);
    font-size: 44px; font-weight: 500; letter-spacing: 10px;
    padding-left: 10px;
  }
  .services-title {
    top: 292px; color: var(--brand-blue);
    font-size: 34px; font-weight: 700;
  }
  .services {
    position: absolute; left: 64px; top: 339px;
    list-style: none;
  }
  .services li {
    position: relative; padding-left: 30px;
    font-size: 25px; line-height: 31.7px; color: var(--ink-black);
    letter-spacing: 0.5px;
  }
  .services li::before {
    content: ""; position: absolute; left: 2px; top: 12px;
    width: 10px; height: 10px; border-radius: 50%;
    background: var(--brand-blue);
  }
  .contact-name {
    top: 680px; color: var(--white);
    font-size: 32px; font-weight: 700; letter-spacing: 0.5px;
  }
  .credentials {
    top: 719px; color: var(--text-dark);
    font-size: 20px; line-height: 26.5px; letter-spacing: 0.5px;
  }
  .contact-divider { position: absolute; left: 104px; top: 806px; }
  .contact-lines {
    top: 837px; color: var(--text-dark);
    font-size: 23px; line-height: 30.5px; letter-spacing: 0.5px;
  }
  .badges { position: absolute; left: 0; top: 944px; }
</style>
</head>
<body>
  <div class="magnet">
    <svg class="magnet__shapes" width="576" height="1009" viewBox="0 0 576 1009">
      <path d="M0 0 H576 V231 Q288 340 0 231 Z" fill="var(--ink-black)"/>
      <circle cx="288" cy="104" r="72" fill="none" stroke="var(--white)" stroke-width="3"/>
      <path d="M0 723 Q288 606 576 723 V934 H0 Z" fill="var(--brand-blue)"/>
    </svg>

    <div class="abs brand-name">NILPOINT TAX</div>

    <div class="abs services-title">Specialising in:</div>
    <ul class="services">
      <li>Small Business Taxation</li>
      <li>Company and Trust Returns</li>
      <li>Financial Statements</li>
      <li>Partnership Taxation</li>
      <li>Individual Income Tax</li>
      <li>BAS Preparation / Lodgement</li>
      <li>Capital Gains Tax</li>
      <li>Business Start Ups</li>
      <li>Business Structuring</li>
      <li>Tax Planning</li>
    </ul>

    <div class="abs contact-name">LIAM CARROW</div>
    <div class="abs credentials">
      CPA, MTAX, BCOM (Acc &amp; Fin)<br>
      Taxation and Business Accountant<br>
      Tax Agent
    </div>

    <svg class="contact-divider" width="370" height="24" viewBox="0 0 370 24">
      <line x1="0" y1="12" x2="125" y2="12" stroke="var(--white)" stroke-width="2"/>
      <line x1="245" y1="12" x2="370" y2="12" stroke="var(--white)" stroke-width="2"/>
      <!-- phone -->
      <path d="M141 4 q-4 2 -2 9 q3 7 8 9 l2 -3 -3 -3 -2 1 q-3 -3 -3 -6 l2 -1 -1 -4 z" fill="var(--white)"/>
      <!-- mail -->
      <rect x="171" y="6" width="18" height="12" fill="var(--white)"/>
      <path d="M171 6 L180 13 L189 6" fill="none" stroke="var(--brand-blue)" stroke-width="1.5"/>
      <!-- globe -->
      <circle cx="218" cy="12" r="8" fill="none" stroke="var(--white)" stroke-width="2"/>
      <ellipse cx="218" cy="12" rx="3.5" ry="8" fill="none" stroke="var(--white)" stroke-width="1.5"/>
      <line x1="210" y1="12" x2="226" y2="12" stroke="var(--white)" stroke-width="1.5"/>
    </svg>

    <div class="abs contact-lines">
      0400 000 123<br>
      liam@nilpointtax.com.au<br>
      www.nilpointtax.com.au
    </div>

    <svg class="badges" width="576" height="50" viewBox="0 0 576 50">
      <circle cx="141" cy="25" r="23" fill="var(--badge-gold)" stroke="#999" stroke-width="1"/>
      <rect x="237" y="2" width="105" height="46" fill="var(--badge-navy)"/>
      <circle cx="437" cy="25" r="23" fill="var(--brand-blue)"/>
    </svg>
  </div>
</body>
</html>
```